Silver Creek Plumbing Business card & letter head design

We need a new business card and letter head for our plumbing company called silver creek plumbing. attached is the companys logo. We provide domestic and commercial plumbing services in regional western Australia. We are after Something simple yet nice to look at and something that fits within the trade industry.

Target Market(s)

trade/building industry

Contact Information for Business Card

Darl Hensby
Manager
0461 238 574
enquiries@scplumbwork.net.au
ABN: 47 381 905 462
PCL: 5187

Domestic & Commercial Plumbing
Tip Truck & Excavator hire

Colors

Designer to choose colors to be used in the design.

```html
<!DOCTYPE html>
<html lang="en">
<head>
<meta charset="utf-8">
<title>Silver Creek Plumbing – Stationery</title>
<link href="https://fonts.googleapis.com/css2?family=Open+Sans:wght@400;600;700&display=swap" rel="stylesheet">
<style>
  :root {
    --bg: #e3e3e4;
    --paper: #f5f5f5;
    --brand-blue: #0e57a3;
    --ink: #4a4a4a;
    --band-grey: #525252;
    --rule: #6a6a6a;
    --white: #ffffff;
  }
  * { margin: 0; padding: 0; box-sizing: border-box; }
  html, body { width: 1200px; height: 1200px; overflow: hidden; }
  body {
    background: var(--bg);
    font-family: "Open Sans", Arial, sans-serif;
    position: relative;
    color: var(--ink);
  }
  .brand-name {
    font-family: "Open Sans", Arial, sans-serif;
    font-weight: 700;
    color: var(--brand-blue);
    white-space: nowrap;
    letter-spacing: -0.2px;
  }

  /* Letterhead */
  .letterhead {
    position: absolute; left: 104px; top: 119px;
    width: 682px; height: 963px;
    background: var(--paper);
  }
  .letterhead .brand-name {
    position: absolute; left: 53px; top: 66px; font-size: 17.5px;
  }
  .letterhead .contact {
    position: absolute; right: 46px; top: 42px;
    text-align: right; font-size: 10.5px; line-height: 14px;
  }
  .contact-line { display: flex; justify-content: flex-end; align-items: center; gap: 3px; }
  .contact-line svg { width: 10px; height: 10px; fill: var(--brand-blue); }
  .reg { margin-top: 6px; }
  .reg .label { color: var(--brand-blue); }
  .letterhead .side-tab {
    position: absolute; right: 0; top: 45px; width: 13px; height: 73px;
    background: var(--brand-blue);
  }
  .service-band { position: absolute; left: 0; right: 0; bottom: 0; }
  .service-band svg { position: absolute; inset: 0; width: 100%; height: 100%; }
  .service-band span {
    position: absolute; top: 50%; transform: translateY(-50%);
    color: var(--white); white-space: nowrap;
  }
  .letterhead .service-band { height: 22px; }
  .letterhead .service-band span { font-size: 10.5px; }
  .letterhead .service-left { left: 54px; }
  .letterhead .service-right { right: 46px; }

  /* Business card front */
  .card-front {
    position: absolute; left: 821px; top: 248px;
    width: 292px; height: 178px;
    background: var(--brand-blue);
    color: var(--white);
  }
  .card-front .brand-name {
    position: absolute; left: 0; right: 0; top: 72px;
    text-align: center; color: var(--white); font-size: 16px;
  }
  .card-front .web {
    position: absolute; left: 0; right: 0; top: 153px;
    text-align: center; font-size: 7.5px; letter-spacing: 1px;
  }
  .card-front .web b { font-weight: 700; }

  /* Business card back */
  .card-back {
    position: absolute; left: 821px; top: 489px;
    width: 292px; height: 179px;
    background: var(--paper);
  }
  .card-back .brand-name { position: absolute; left: 18px; top: 34px; font-size: 12px; }
  .card-back .person {
    position: absolute; right: 19px; top: 92px; text-align: right;
  }
  .person-name { font-size: 11px; font-weight: 700; color: var(--brand-blue); line-height: 13px; }
  .person-role { font-size: 7px; line-height: 9px; }
  .card-back .name-rule {
    position: absolute; left: 19px; top: 114px; width: 220px; height: 0;
    border-top: 0.7px solid var(--rule);
  }
  .card-back .side-tab {
    position: absolute; right: 0; top: 94px; width: 9px; height: 23px;
    background: var(--brand-blue);
  }
  .card-back .details {
    position: absolute; left: 19px; top: 127px; font-size: 6.6px; line-height: 9.6px;
  }
  .card-back .details .contact-line { justify-content: flex-start; }
  .card-back .details svg { width: 6.5px; height: 6.5px; }
  .card-back .regs {
    position: absolute; right: 19px; top: 136.5px; text-align: right;
    font-size: 6.6px; line-height: 9.6px;
  }
  .card-back .regs .label { color: var(--brand-blue); }
  .card-back .service-band { height: 13px; }
  .card-back .service-band span { font-size: 6.8px; }
  .card-back .service-left { left: 19px; }
  .card-back .service-right { right: 19px; }
</style>
</head>
<body>

<svg width="0" height="0" style="position:absolute">
  <defs>
    <symbol id="icon-phone" viewBox="0 0 24 24"><path d="M6.6 10.8a15.2 15.2 0 0 0 6.6 6.6l2.2-2.2a1 1 0 0 1 1-.25 11.4 11.4 0 0 0 3.6.57 1 1 0 0 1 1 1V20a1 1 0 0 1-1 1A17 17 0 0 1 3 4a1 1 0 0 1 1-1h3.5a1 1 0 0 1 1 1c0 1.25.2 2.45.57 3.57a1 1 0 0 1-.25 1z"/></symbol>
    <symbol id="icon-mail" viewBox="0 0 24 24"><path d="M2 4h20v16H2zm2 2v.5l8 5.5 8-5.5V6zm0 3v9h16V9l-8 5.5z"/></symbol>
    <symbol id="icon-web" viewBox="0 0 24 24"><path d="M12 2a10 10 0 1 0 0 20 10 10 0 0 0 0-20zm6.9 6h-2.9a15 15 0 0 0-1.3-3.6A8 8 0 0 1 18.9 8zM12 4c.8 1.2 1.5 2.5 1.9 4h-3.8c.4-1.5 1.1-2.8 1.9-4zM4.3 14a8 8 0 0 1 0-4h3.4a16 16 0 0 0 0 4zm.8 2h2.9c.3 1.3.8 2.5 1.3 3.6A8 8 0 0 1 5.1 16zM8 8H5.1a8 8 0 0 1 4.2-3.6C8.8 5.5 8.3 6.7 8 8zm4 12c-.8-1.2-1.5-2.5-1.9-4h3.8c-.4 1.5-1.1 2.8-1.9 4zm2.3-6H9.7a14 14 0 0 1 0-4h4.6a14 14 0 0 1 0 4zm.4 5.6c.5-1.1 1-2.3 1.3-3.6h2.9a8 8 0 0 1-4.2 3.6zM16.3 14a16 16 0 0 0 0-4h3.4a8 8 0 0 1 0 4z"/></symbol>
  </defs>
</svg>

<section class="letterhead">
  <div class="brand-name">Silver Creek Plumbing</div>
  <div class="contact">
    <div class="contact-line">0461 238 574 <svg><use href="#icon-phone"/></svg></div>
    <div class="contact-line">enquiries@scplumbwork.net.au <svg><use href="#icon-mail"/></svg></div>
    <div class="contact-line">www.scplumbwork.net.au <svg><use href="#icon-web"/></svg></div>
    <div class="reg">
      <div><span class="label">ABN:</span> 47 381 905 462</div>
      <div><span class="label">PCL:</span> 5187</div>
    </div>
  </div>
  <div class="side-tab"></div>
  <div class="service-band">
    <svg viewBox="0 0 682 22" preserveAspectRatio="none">
      <polygon points="0,0 420,0 412,22 0,22" fill="var(--band-grey)"/>
      <polygon points="424,0 682,0 682,22 416,22" fill="var(--brand-blue)"/>
    </svg>
    <span class="service-left">DOMESTIC &amp; COMMERCIAL PLUMBING</span>
    <span class="service-right">TIP TRUCK &amp; EXCAVATOR HIRE</span>
  </div>
</section>

<section class="card-front">
  <div class="brand-name">Silver Creek Plumbing</div>
  <div class="web">www.<b>scplumbwork</b>.net.au</div>
</section>

<section class="card-back">
  <div class="brand-name">Silver Creek Plumbing</div>
  <div class="person">
    <div class="person-name">Darl Hensby</div>
    <div class="person-role">Manager</div>
  </div>
  <div class="name-rule"></div>
  <div class="side-tab"></div>
  <div class="details">
    <div class="contact-line"><svg><use href="#icon-phone"/></svg> 0461 238 574</div>
    <div class="contact-line"><svg><use href="#icon-mail"/></svg> enquiries@scplumbwork.net.au</div>
    <div class="contact-line"><svg><use href="#icon-web"/></svg> www.scplumbwork.net.au</div>
  </div>
  <div class="regs">
    <div><span class="label">ABN:</span> 47 381 905 462</div>
    <div><span class="label">PCL:</span> 5187</div>
  </div>
  <div class="service-band">
    <svg viewBox="0 0 292 13" preserveAspectRatio="none">
      <polygon points="0,0 165,0 161,13 0,13" fill="var(--band-grey)"/>
      <polygon points="168,0 292,0 292,13 164,13" fill="var(--brand-blue)"/>
    </svg>
    <span class="service-left">Domestic &amp; Commercial Plumbing</span>
    <span class="service-right">Tip Truck &amp; Excavator Hire</span>
  </div>
</section>

</body>
</html>
```